Wheelchair Accessible Accommodation

We are 100% online, promoting accommodation details and booking facilities for wheelchair dependant travellers.
Listings will only be accommodation providers which meet our specific criteria.

Target Market(s)

Wheelchair dependant people and their companions

Industry/Entity Type

Accommodation

Contact Information for Business Card

Name, mobile phone number, email address, website address

```html
<!DOCTYPE html>
<html lang="en">
<head>
<meta charset="utf-8">
<title>Level Access Stays – Business Card</title>
<link rel="stylesheet" href="https://fonts.googleapis.com/css2?family=Montserrat:wght@600;700;800&family=Didact+Gothic&display=swap">
<style>
  :root {
    --bg: #222222;
    --card: #f1f1f1;
    --card-edge: #e2e2e2;
    --red: #ed1c24;
    --black: #1a1a1a;
    --text: #2b2b2b;
  }
  * { margin: 0; padding: 0; box-sizing: border-box; }
  html, body { width: 1200px; height: 900px; overflow: hidden; }
  body {
    background: var(--bg);
    position: relative;
    font-family: "Didact Gothic", sans-serif;
    color: var(--text);
  }
  .card {
    position: absolute;
    left: 340px;
    width: 520px;
    height: 290px;
    background: linear-gradient(135deg, #ffffff 0%, var(--card) 60%, var(--card-edge) 100%);
    overflow: hidden;
    box-shadow: 0 12px 30px rgba(0,0,0,0.5);
  }
  .card--back { top: 135px; }
  .card--front { top: 475px; }
  .card__art { position: absolute; inset: 0; }

  .brand {
    position: absolute;
    display: flex;
    align-items: center;
    gap: 10px;
    font-family: "Montserrat", sans-serif;
    font-weight: 800;
    color: var(--red);
    letter-spacing: -0.5px;
    line-height: 1;
  }
  .brand__dot {
    border-radius: 50%;
    background: var(--black);
    flex: none;
  }
  .card--back .brand { left: 200px; top: 100px; font-size: 34px; }
  .card--back .brand__dot { width: 26px; height: 26px; }
  .card--front .brand { left: 40px; top: 52px; font-size: 24px; }
  .card--front .brand__dot { width: 20px; height: 20px; }

  .website-tag {
    position: absolute;
    left: 236px;
    top: 160px;
    font-size: 20px;
    color: var(--black);
  }

  .person {
    position: absolute;
    left: 300px;
    top: 80px;
    font-family: "Montserrat", sans-serif;
  }
  .person__name { font-size: 28px; font-weight: 800; letter-spacing: -0.5px; }
  .person__name .first { color: var(--red); }
  .person__name .last { color: var(--black); }
  .person__role { font-size: 17px; font-weight: 700; color: var(--black); margin-top: 14px; }

  .contacts {
    position: absolute;
    left: 300px;
    top: 160px;
    list-style: none;
  }
  .contacts__item {
    display: flex;
    align-items: center;
    gap: 18px;
    height: 32px;
    font-size: 19px;
    letter-spacing: 1.5px;
  }
  .contacts__icon { width: 22px; height: 22px; flex: none; }
</style>
</head>
<body>

  <section class="card card--back" aria-label="Card back">
    <svg class="card__art" viewBox="0 0 520 290" aria-hidden="true">
      <polygon points="0,0 118,0 18,290 0,290" fill="var(--red)"/>
      <polygon points="128,0 141,0 41,290 28,290" fill="var(--black)"/>
    </svg>
    <div class="brand"><span class="brand__dot"></span>Level Access Stays</div>
    <p class="website-tag">your website here</p>
  </section>

  <section class="card card--front" aria-label="Card front">
    <svg class="card__art" viewBox="0 0 520 290" aria-hidden="true">
      <rect x="440" y="0" width="7" height="88" fill="var(--black)"/>
      <rect x="458" y="0" width="7" height="88" fill="var(--red)"/>
      <rect x="300" y="122" width="220" height="3" fill="var(--black)"/>
      <rect x="50" y="175" width="7" height="115" fill="var(--black)"/>
      <rect x="68" y="175" width="7" height="115" fill="var(--red)"/>
    </svg>

    <div class="brand"><span class="brand__dot"></span>Level Access Stays</div>

    <div class="person">
      <p class="person__name"><span class="first">Your</span><span class="last">Name</span></p>
      <p class="person__role">Designation</p>
    </div>

    <ul class="contacts">
      <li class="contacts__item">
        <svg class="contacts__icon" viewBox="0 0 22 22" aria-hidden="true">
          <rect x="1" y="1" width="20" height="20" rx="4" fill="var(--black)"/>
          <path d="M7 5c-1 1-1.5 2.5-.5 4.5 1.3 2.8 3.5 5 6.3 6.5 2 1 3.5.5 4.5-.5l-2-2.2-1.8 1c-1.6-.8-3.3-2.5-4.1-4.1l1-1.8z" fill="#fff"/>
        </svg>
        Phone Number
      </li>
      <li class="contacts__item">
        <svg class="contacts__icon" viewBox="0 0 22 22" aria-hidden="true">
          <rect x="1" y="5" width="20" height="13" fill="var(--black)"/>
          <path d="M1.5 5.5 11 12.5 20.5 5.5" fill="none" stroke="#fff" stroke-width="1.3"/>
        </svg>
        E-mail Addres
      </li>
      <li class="contacts__item">
        <svg class="contacts__icon" viewBox="0 0 22 22" aria-hidden="true" fill="none" stroke="var(--black)" stroke-width="1.3">
          <circle cx="11" cy="11" r="8.5"/>
          <ellipse cx="11" cy="11" rx="3.8" ry="8.5"/>
          <path d="M2.5 11h17M4 6.5h14M4 15.5h14"/>
        </svg>
        Website
      </li>
    </ul>
  </section>

</body>
</html>
```